Plakat-Design für Tanzkurse in Salsa, Bachata, Kizomba & Zouk
Zielgruppe
Tanzkurse in Salsa, Bachata, Kizomba & Zouk
Zielgruppe 20-45 Arbeitstätig & Studenten
Wir bieten in den oben genannten Tänzen mit Spezialisierten internationalen Trainern und Trainerinnen didaktisch & methodisch hochwertige Tanzkurse an.
Aufgabenstellung
Inhalte:
DIN A1
Es soll auf Gutscheine 'Tanzgutscheine' zu Weihnachten hingewiesen werden und Lust auf einen Tanzkurs bei uns machen.
Es soll edel, professionell, und farblich harmonisch sein. Keine Chilis, kein Kuban Feeling!
Mögliches Bildmaterial ist im Anhang zu finden.
Farbe Logo: #A82068
Weitere verwendete Farben: #0A8694

```html
<!DOCTYPE html>
<html lang="de">
<head>
<meta charset="utf-8">
<title>Tanzkurse – Plakat</title>
<link href="https://fonts.googleapis.com/css2?family=Roboto+Condensed:wght@300;400;700&display=swap" rel="stylesheet">
<style>
  :root {
    --page: #e9e8e6;
    --magenta: #a82068;
    --magenta-deep: #8e1a57;
    --gold: #e3b23c;
    --gold-dark: #b8862a;
    --mauve-top: #8a7888;
    --mauve-mid: #cfc7cf;
    --mauve-bottom: #766478;
    --ink: #1f1a21;
    --white: #ffffff;
  }
  * { box-sizing: border-box; margin: 0; padding: 0; }
  html, body {
    width: 1200px; height: 900px; overflow: hidden;
    background: var(--page);
    font-family: "Roboto Condensed", "Arial Narrow", sans-serif;
  }
  .poster {
    position: absolute; left: 303px; top: 30px;
    width: 594px; height: 840px; overflow: hidden;
    box-shadow: 0 6px 18px rgba(0,0,0,.18);
  }
  .poster__photo {
    position: absolute; inset: 0;
    background:
      radial-gradient(ellipse 60% 45% at 55% 40%, rgba(245,240,242,.85), rgba(245,240,242,0) 70%),
      linear-gradient(180deg, var(--mauve-top) 0%, var(--mauve-mid) 35%, #b7abb6 60%, var(--mauve-bottom) 100%);
  }
  .brand {
    position: absolute; top: 38px; left: 0; right: 0;
    display: flex; flex-direction: column; align-items: center;
  }
  .brand__row { display: flex; align-items: center; gap: 14px; }
  .brand__name {
    font-size: 34px; font-weight: 400; color: var(--magenta);
    letter-spacing: .5px;
  }
  .brand__dot { width: 34px; height: 34px; border-radius: 50%; background: var(--magenta); }
  .brand__tagline {
    margin-top: 2px; font-size: 12px; color: #3b3040; letter-spacing: .6px;
  }
  .headline {
    position: absolute; top: 278px; left: 0; right: 0;
    text-align: center; font-size: 60px; font-weight: 700;
    color: var(--magenta); letter-spacing: .5px;
  }
  .styles {
    position: absolute; top: 382px; left: 78px; right: 78px;
    border-top: 1px solid rgba(255,255,255,.8);
    border-bottom: 1px solid rgba(255,255,255,.8);
    padding: 14px 0 16px; text-align: center;
    color: var(--white); font-size: 26px; font-weight: 400; letter-spacing: 6px;
  }
  .voucher {
    position: absolute; left: 42px; top: 526px;
    width: 196px; height: 196px; border-radius: 50%;
    background: var(--magenta);
    border: 7px solid var(--gold);
    box-shadow: 0 0 0 2px var(--gold-dark), 0 4px 10px rgba(0,0,0,.25);
    display: flex; flex-direction: column; align-items: center; justify-content: center;
    text-align: center; color: var(--white); padding: 0 18px;
  }
  .voucher__lead { font-size: 18px; line-height: 1.2; }
  .voucher__title { margin-top: 6px; font-size: 19px; font-weight: 700; color: var(--gold); letter-spacing: .5px; }
  .voucher__note { margin-top: 6px; font-size: 13px; line-height: 1.25; }
  .address {
    position: absolute; right: 42px; top: 634px;
    text-align: right; color: var(--white); font-size: 15px; line-height: 29px;
  }
  .address__school { font-weight: 700; }
  .contact {
    position: absolute; right: 42px; top: 734px;
    color: var(--white); font-size: 15px;
  }
  .website {
    position: absolute; left: 0; right: 0; top: 772px;
    text-align: center; font-size: 44px; font-weight: 400;
    color: var(--ink); letter-spacing: .5px;
  }
</style>
</head>
<body>
  <article class="poster">
    <div class="poster__photo" role="img" aria-label="Foto: Tanzpaar dreht sich in einem hellen Raum mit großen Fenstern"></div>

    <header class="brand">
      <div class="brand__row">
        <span class="brand__name">Baile Luminoso</span>
        <span class="brand__dot"></span>
      </div>
      <div class="brand__tagline">Salsa · Bachata · Kizomba</div>
    </header>

    <h1 class="headline">TANZKURSE</h1>
    <p class="styles">SALSA • BACHATA • KIZOMBA</p>

    <aside class="voucher">
      <p class="voucher__lead">Die Geschenkidee<br>zu Weihnachten:</p>
      <p class="voucher__title">TANZGUTSCHEIN</p>
      <p class="voucher__note">Verschenke ein paar Stunden<br>gemeinsamen Spaß.</p>
    </aside>

    <address class="address">
      <div class="address__school">Tanzschule Baile Luminoso</div>
      <div>Lindenweg 14 &amp; weitere Locations</div>
      <div>79100 Musterstadt am Rhein</div>
    </address>
    <p class="contact">hallo@baile-luminoso.de | T +49 151 000 482 16</p>

    <p class="website">WWW.BAILE-LUMINOSO.DE</p>
  </article>
</body>
</html>
```